Harborline Stay Collective Business Card Design

Design a business card for Harborline Stay Collective. Look at the website for colors and reference. Card should have logo, name, title, office number, mobile number, email, URL and a tagline like, "Luxury Hotel & Resort Email Marketing" (This might change).

https://www.harborlinestaycollective.net

The rest I will leave up to your imagination.

Contact Information for Business Card

Logo, name, title, office number, mobile number, email, URL and a tagline like, "Luxury Hotel & Resort Email Marketing" (This might change).

```html
<!DOCTYPE html>
<html lang="en">
<head>
<meta charset="utf-8">
<title>Harborline Stay Collective – Business Card</title>
<link rel="stylesheet" href="https://fonts.googleapis.com/css2?family=Open+Sans:wght@400;600;700&display=swap">
<style>
  :root {
    --bg-light: #c9c8c8;
    --bg-dark: #9e9d9d;
    --card-black: #111111;
    --card-charcoal: #2a2a2a;
    --card-white: #ffffff;
    --accent-orange: #f47d20;
    --text-white: #f2f2f2;
    --text-dark: #141414;
    --text-muted: #555555;
  }
  * { margin: 0; padding: 0; box-sizing: border-box; }
  html, body { width: 1200px; height: 876px; overflow: hidden; }
  body {
    background: radial-gradient(ellipse at 50% 40%, var(--bg-light) 0%, var(--bg-dark) 100%);
    font-family: "Open Sans", Arial, sans-serif;
    position: relative;
  }
  .card {
    position: absolute;
    top: 288px;
    width: 525px;
    height: 300px;
    overflow: hidden;
    box-shadow: 0 10px 24px rgba(0,0,0,0.35);
  }
  .card-front { left: 50px; background: var(--card-white); }
  .card-back {
    left: 625px;
    background: radial-gradient(ellipse at 38% 55%, var(--card-charcoal) 0%, var(--card-black) 70%);
  }
  .front-shape { position: absolute; inset: 0; }
  .contact-block {
    position: absolute;
    left: 30px;
    top: 28px;
    color: var(--text-white);
  }
  .person-name {
    color: var(--accent-orange);
    font-size: 19px;
    font-weight: 600;
    letter-spacing: 0.3px;
    text-transform: uppercase;
    line-height: 1.1;
  }
  .person-title { font-size: 12px; margin-top: 2px; }
  .address { font-size: 11px; line-height: 1.35; margin-top: 22px; }
  .contact-list { list-style: none; margin-top: 20px; }
  .contact-list li {
    display: flex;
    align-items: center;
    gap: 9px;
    font-size: 12px;
    line-height: 22px;
    white-space: nowrap;
  }
  .contact-list svg { width: 12px; height: 12px; flex: none; }
  .brand {
    position: absolute;
    display: flex;
    align-items: center;
    gap: 10px;
    font-weight: 700;
    text-transform: uppercase;
    line-height: 1.05;
    letter-spacing: 1px;
  }
  .brand-mark { width: 13px; height: 13px; background: var(--accent-orange); flex: none; }
  .brand-front { left: 338px; top: 118px; color: var(--text-dark); font-size: 17px; }
  .tagline {
    position: absolute;
    left: 361px;
    top: 168px;
    width: 150px;
    font-size: 10px;
    line-height: 1.35;
    color: var(--text-muted);
  }
  .brand-back {
    left: 50%; top: 50%;
    transform: translate(-50%, -50%);
    color: var(--text-white);
    font-size: 28px;
    white-space: nowrap;
  }
</style>
</head>
<body>

<section class="card card-front" aria-label="Business card front">
  <svg class="front-shape" viewBox="0 0 525 300" width="525" height="300" aria-hidden="true">
    <defs>
      <linearGradient id="frontBlack" x1="0" y1="0" x2="1" y2="1">
        <stop offset="0" stop-color="#1c1c1c"/>
        <stop offset="0.5" stop-color="#2b2b2b"/>
        <stop offset="1" stop-color="#0e0e0e"/>
      </linearGradient>
    </defs>
    <path d="M0 0 H330 C260 55 240 170 345 300 H0 Z" fill="url(#frontBlack)"/>
    <path d="M320 6 C257 60 241 160 313 280" fill="none" stroke="#3a3a3a" stroke-width="5" stroke-linecap="round"/>
    <path d="M337 4 C277 55 259 150 307 250" fill="none" stroke="var(--accent-orange)" stroke-width="5" stroke-linecap="round"/>
  </svg>

  <div class="contact-block">
    <p class="person-name">Daniel Moreno</p>
    <p class="person-title">Manager</p>
    <p class="address">Your address, city<br>state, ZIP 0000</p>
    <ul class="contact-list">
      <li>
        <svg viewBox="0 0 12 12"><path d="M3 1 L5 3.5 L4 5 C4.8 6.6 5.6 7.4 7 8 L8.5 7 L11 9 L9.5 11 C5 10.5 1.5 7 1 2.5 Z" fill="var(--accent-orange)"/></svg>
        123-456-2100
      </li>
      <li>
        <svg viewBox="0 0 12 12"><rect x="3" y="0.8" width="6" height="10.4" rx="1" fill="none" stroke="var(--accent-orange)" stroke-width="1.3"/><circle cx="6" cy="9.2" r="0.7" fill="var(--accent-orange)"/></svg>
        123-456-2100
      </li>
      <li>
        <svg viewBox="0 0 12 12"><rect x="1" y="2.5" width="10" height="7" fill="none" stroke="var(--accent-orange)" stroke-width="1.2"/><path d="M1 2.5 L6 6.5 L11 2.5" fill="none" stroke="var(--accent-orange)" stroke-width="1.2"/></svg>
        hello@harborlinestay.net
      </li>
      <li>
        <svg viewBox="0 0 12 12"><circle cx="6" cy="6" r="5" fill="none" stroke="var(--accent-orange)" stroke-width="1.2"/><ellipse cx="6" cy="6" rx="2" ry="5" fill="none" stroke="var(--accent-orange)" stroke-width="1"/><path d="M1 6 H11" stroke="var(--accent-orange)" stroke-width="1"/></svg>
        www.harborlinestaycollective.net
      </li>
    </ul>
  </div>

  <div class="brand brand-front">
    <span class="brand-mark"></span>
    <span>Harborline<br>Stay Collective</span>
  </div>
  <p class="tagline">Luxury Hotel &amp; Resort Email Marketing</p>
</section>

<section class="card card-back" aria-label="Business card back">
  <div class="brand brand-back">
    <span class="brand-mark"></span>
    <span>Harborline Stay Collective</span>
  </div>
</section>

</body>
</html>
```